Real Estate Seller Financing Postcard

I need a postcard that lays out these options contained in the notes that grabs attention, explains the two options easily and is eye-catching. The front needs to have the percentages on it and information about it and on the other side One side exact Text is:
"Monthly income without tenant headaches" in big letters. Also on front "Get
110%
add an "or"
160% of market value for your property. ". The percentages should be displayed and that is not to be a sentence of text. Other side text: I need bullets points for these "Formal protection as a lien holder against home
No commission or closing cost
Fast closings possible
Property taken as is so no repairs.

Add to the top of the back in "It’s simple. I am a new investor without down payment capital who still want to double our portfolio this year to grow our portfolio."
Here are the two options that are to be the largest part of the back
Option 1, you can receive 80% now cash and 30% over a short period of time including interest.

Option 2, where act like a bank allowing you to make 150% if you finance the whole property(ies). No gimmicks and surprises, just simple unconventional financing.

Include Logo Somewhere

Target Market(s)

Property Owners Wanting to Sell Their Property

Industry/Entity Type

Real Estate Investing

Requirements
Must have
• The options promiment and each side with its respective information. Must have logo somewhere
Nice to have
• The options in color other than black.
Should not have
• A picture of money on the front. Any other image is okay.

```html
<!DOCTYPE html>
<html lang="en">
<head>
<meta charset="utf-8">
<title>Seller Financing Postcard</title>
<link rel="stylesheet" href="https://fonts.googleapis.com/css2?family=Montserrat:wght@700;800;900&family=Arimo:wght@400&display=swap">
<style>
  :root {
    --ink: #08323f;
    --orange: #ef7622;
    --slate: #525c58;
    --white: #ffffff;
    --paper: #e9e7e3;
    --navy: #1e3a8a;
  }
  * { box-sizing: border-box; margin: 0; padding: 0; }
  html, body { width: 900px; height: 1200px; overflow: hidden; background: var(--paper); }
  body { position: relative; font-family: "Montserrat", sans-serif; }

  .card {
    position: absolute; left: 40px; width: 820px; height: 540px;
    background: var(--ink); overflow: hidden;
    box-shadow: 0 6px 18px rgba(0,0,0,.25);
  }
  .card--front { top: 40px; }
  .card--back { top: 620px; }

  /* Front */
  .brand {
    position: absolute; left: 36px; top: 36px; width: 170px; height: 170px;
    background: var(--white); display: flex; align-items: center; justify-content: center; gap: 8px;
    padding: 12px;
  }
  .brand__mark { width: 14px; height: 14px; border-radius: 50%; background: var(--navy); flex: none; }
  .brand__name { font-weight: 800; font-size: 15px; line-height: 1.15; color: var(--navy); }

  .headline {
    position: absolute; left: 220px; top: 50px; width: 580px;
    text-align: center; color: var(--orange); font-weight: 900;
    font-size: 32px; line-height: 1.15; text-transform: uppercase;
  }

  .offer {
    position: absolute; left: 36px; top: 220px;
    display: flex; align-items: flex-end; gap: 12px;
    color: var(--orange); font-weight: 800; text-transform: uppercase;
  }
  .offer__word { font-size: 28px; line-height: 1; padding-bottom: 10px; }
  .offer__tail { font-size: 25px; line-height: 1.15; padding-bottom: 8px; }
  .pct-arrow { display: block; }
  .pct-arrow text { font-family: "Montserrat", sans-serif; font-weight: 800; font-size: 21px; }

  .benefits {
    position: absolute; left: 40px; top: 390px; list-style: none;
    font-family: "Arimo", sans-serif; color: var(--white); font-size: 22px; line-height: 1.45;
  }
  .benefits li::before { content: "•"; margin-right: 8px; }

  .growth-art {
    position: absolute; right: 0; bottom: 0; width: 210px; height: 330px;
    background: linear-gradient(160deg, var(--slate) 0%, var(--orange) 70%);
    clip-path: polygon(45% 0, 75% 8%, 100% 20%, 100% 100%, 0 100%, 15% 35%);
  }

  /* Back */
  .skyline-art {
    position: absolute; left: 0; top: 140px; width: 200px; height: 150px;
    background: linear-gradient(135deg, #ffffff 0%, #c9ccd1 55%, #7d828a 100%);
  }
  .intro {
    position: absolute; left: 220px; top: 30px; width: 570px;
    text-align: center; color: var(--white); font-weight: 800;
    font-size: 14px; line-height: 1.35; text-transform: uppercase;
  }
  .intro__lead { color: var(--slate); font-weight: 900; font-size: 40px; line-height: 1.1; margin-right: 6px; }

  .option-band {
    position: absolute; left: 0; top: 290px; width: 100%; height: 120px;
    background: var(--orange);
  }
  .option-band__row {
    position: absolute; left: 0; right: 0; bottom: 64px;
    display: flex; justify-content: center; align-items: flex-end; gap: 14px;
    color: var(--ink); font-weight: 800; font-size: 24px; line-height: 1;
    text-transform: uppercase; white-space: nowrap;
  }
  .option-band__row span { padding-bottom: 2px; }
  .drop { display: block; flex: none; }
  .option-band__line {
    position: absolute; left: 0; right: 0; top: 70px; text-align: center;
    color: var(--ink); font-weight: 800; font-size: 23px; line-height: 1.2;
    text-transform: uppercase; white-space: nowrap;
  }

  .option-two {
    position: absolute; left: 30px; top: 424px; width: 660px;
    text-align: center; color: var(--orange); font-weight: 800;
    font-size: 21px; line-height: 1.25; text-transform: uppercase;
  }
  .point-150 { position: absolute; right: 0; top: 424px; }
</style>
</head>
<body>

<section class="card card--front" aria-label="Postcard front">
  <div class="brand">
    <span class="brand__mark"></span>
    <span class="brand__name">Helios Property Group</span>
  </div>

  <h1 class="headline">Monthly income<br>without tenant headaches</h1>

  <div class="offer">
    <span class="offer__word">Get</span>
    <svg class="pct-arrow" width="62" height="150" viewBox="0 0 62 150" aria-label="110%">
      <polygon points="31,0 62,42 48,42 48,150 14,150 14,42 0,42" fill="var(--slate)"/>
      <text x="31" y="100" fill="var(--orange)" text-anchor="middle" dominant-baseline="middle" transform="rotate(-90 31 100)">110%</text>
    </svg>
    <span class="offer__word">or</span>
    <svg class="pct-arrow" width="62" height="150" viewBox="0 0 62 150" aria-label="160%">
      <polygon points="31,0 62,42 48,42 48,150 14,150 14,42 0,42" fill="var(--slate)"/>
      <text x="31" y="100" fill="var(--orange)" text-anchor="middle" dominant-baseline="middle" transform="rotate(-90 31 100)">160%</text>
    </svg>
    <span class="offer__tail">Of market value<br>for your property</span>
  </div>

  <ul class="benefits">
    <li>Formal protection as a lien holder against home</li>
    <li>No commission or closing cost</li>
    <li>Fast closings possible</li>
    <li>Property taken as is so no repairs</li>
  </ul>

  <div class="growth-art" role="img" aria-label="Illustration of rising house-shaped arrows"></div>
</section>

<section class="card card--back" aria-label="Postcard back">
  <div class="skyline-art" role="img" aria-label="Illustration of city office towers"></div>

  <p class="intro"><span class="intro__lead">It's simple.</span> I am a new investor<br>without down payment<br>capital who still want to double<br>our portfolio this year to grow our portfolio</p>

  <div class="option-band">
    <div class="option-band__row">
      <span>You can receive</span>
      <svg class="drop" width="56" height="110" viewBox="0 0 56 110" aria-label="80%">
        <polygon points="12,0 44,0 44,70 56,70 28,110 0,70 12,70" fill="var(--slate)"/>
        <text x="28" y="38" fill="var(--white)" font-family="Montserrat, sans-serif" font-weight="800" font-size="20" text-anchor="middle" dominant-baseline="middle" transform="rotate(-90 28 38)">80%</text>
      </svg>
      <span>now cash and</span>
      <svg class="drop" width="56" height="110" viewBox="0 0 56 110" aria-label="30%">
        <polygon points="12,0 44,0 44,70 56,70 28,110 0,70 12,70" fill="var(--slate)"/>
        <text x="28" y="38" fill="var(--white)" font-family="Montserrat, sans-serif" font-weight="800" font-size="20" text-anchor="middle" dominant-baseline="middle" transform="rotate(-90 28 38)">30%</text>
      </svg>
    </div>
    <p class="option-band__line">over a short period of time including interest</p>
  </div>

  <svg class="point-150" width="115" height="46" viewBox="0 0 115 46" aria-label="150%">
    <polygon points="0,23 32,0 32,9 115,9 115,37 32,37 32,46" fill="var(--slate)"/>
    <text x="74" y="24" fill="var(--orange)" font-family="Montserrat, sans-serif" font-weight="800" font-size="19" text-anchor="middle" dominant-baseline="middle">150%</text>
  </svg>

  <p class="option-two">Where act like a bank allowing you to make<br>if you finance the whole property(ies).<br>No gimmicks and surprises,<br>just simple unconventional financing</p>
</section>

</body>
</html>
```